School Fairs flyer design

We are running school fairs (Brightpath Residential Academies Expo in East Africa) in February 2018. The school fairs and information sessions will take place in Rwanda (February 6th-8th, Kenya February 9th-10th and Uganda on February 11th-12th.)

Rwanda:
Kigali School Fair: February 7th, 1:30-5:30PM
Student Interviews: February 8th, 9:00-1PM
Location: Kigali Moravel Hotel

For information:
Phone number: +250795142867
Email: info@tpwadvisors.com
www.tpwlearningadvisors.com

Features:
*6 US Boarding Schools representative
*Learn about the application process and apply in person.
* Bring your transcripts/school reports to Interview
* www.tpwlearningadvisors.com

Target Market(s)

Students age 11-20 and their parents

Industry/Entity Type

Education

Contact Information for Business Card

Mathieu Rukundobwa
Executive Director
TPW Advisors
Dallas, Texas
Mathieu@tpwadvisers.com
www.tpwadvisors.com
+1937-285-6193

Number of Pages Required

4 page

Font styles to use
Serif

Colors

Designer to choose colors to be used in the design.

Requirements
Must have
• Very clean, elegant and professional designs. Since we offer educational services to students and families, school tours and fairs, as well as institutional support. We would like the designs to reflect what we do.
Nice to have
• Global view, a new logo that incorporates things from our existing logo. We will use this more often but the targeted population is the same.
Should not have
• off colors

```html
<!DOCTYPE html>
<html lang="en">
<head>
<meta charset="utf-8">
<title>Brightpath Residential Academies Expo – East Africa 2018</title>
<link rel="stylesheet" href="https://fonts.googleapis.com/css2?family=Lato:wght@400;700;900&display=swap">
<style>
  :root{
    --stage:#ecebe8;
    --sun:#fbbf1e;
    --sun-pale:#fde39a;
    --cream:#fdf3d8;
    --cream-deep:#fbe6b0;
    --orange:#ea8a3f;
    --orange-title:#e8893a;
    --brown:#6b4a2e;
    --ink:#3a3330;
    --white:#ffffff;
    --rw-blue:#20a0de;--rw-yellow:#f9d616;--rw-green:#1f6a3b;
    --ke-black:#111111;--ke-red:#bb1f2a;--ke-green:#1a7a3a;
    --ug-black:#111111;--ug-yellow:#fcdc04;--ug-red:#d90000;
  }
  *{box-sizing:border-box;margin:0;padding:0}
  html,body{width:900px;height:1200px;overflow:hidden}
  body{background:var(--stage);font-family:"Lato",sans-serif;position:relative}
  .flyer{position:absolute;left:124px;top:50px;width:653px;height:1077px;overflow:hidden;
    background:linear-gradient(to bottom,var(--white) 0,var(--white) 420px,var(--cream) 640px,var(--cream-deep) 920px);
    box-shadow:0 4px 14px rgba(0,0,0,.25)}
  .header-band{position:absolute;left:0;top:0;width:100%;height:236px;background:var(--sun)}
  .header-edge{position:absolute;left:0;top:236px;width:100%;height:6px;background:var(--sun-pale)}
  .globe-deco{position:absolute;border-radius:50%}
  .globe-top{left:430px;top:-15px;width:170px;height:170px;background:rgba(255,255,255,.35)}
  .globe-mid{left:195px;top:490px;width:270px;height:270px;background:rgba(240,190,140,.22)}
  .globe-foot{left:25px;top:925px;width:150px;height:150px;background:rgba(255,255,255,.14)}
  .headline{position:absolute;left:58px;top:34px;color:var(--white);font-weight:700;font-size:18.5px;line-height:24px}
  .photo-frame{position:absolute;left:49px;top:85px;width:554px;height:305px;background:var(--white);padding:8px;display:flex;gap:3px}
  .portrait{flex:1;height:100%;background:linear-gradient(to bottom,#cfcfcf,#a8948a 55%,#e9d9b8)}
  .brand-badge{position:absolute;left:243px;top:295px;width:166px;height:92px;background:var(--white);border-radius:83px 83px 0 0;
    display:flex;align-items:center;justify-content:center;gap:6px;padding-top:14px}
  .brand-dot{width:14px;height:14px;border-radius:50%;background:var(--orange)}
  .brand-name{font-weight:900;font-size:15px;color:#1c4f8a}
  .event-title{position:absolute;left:0;top:418px;width:100%;text-align:center;color:var(--orange-title);font-weight:700;font-size:22px;line-height:31px}
  .country-band{position:absolute;left:0;top:590px;width:100%;height:57px;background:var(--orange)}
  .stop{position:absolute;width:190px;transform:rotate(20deg);transform-origin:95px 90px;text-align:center;color:var(--brown)}
  .stop-name{font-weight:700;font-size:17px;height:24px}
  .flag-card{width:180px;height:126px;margin:0 auto;background:var(--white);padding:6px;box-shadow:2px 3px 6px rgba(0,0,0,.35)}
  .flag-card svg{display:block;width:100%;height:100%}
  .stop-dates{font-weight:700;font-size:16px;margin-top:6px}
  .stop-details{font-size:8.5px;line-height:10.5px;text-align:left;padding-left:8px}
  .stop-details b{font-weight:700}
  .features{position:absolute;left:0;top:796px;width:100%;text-align:center;color:var(--ink);font-size:11.5px;line-height:16px}
  .services{position:absolute;left:0;top:854px;width:100%;text-align:center;color:var(--ink);font-size:12px;line-height:16px;word-spacing:1px}
  .contact-band{position:absolute;left:0;top:918px;width:100%;height:115px;background:var(--orange)}
  .contact{position:absolute;left:0;top:928px;width:100%;text-align:center;color:var(--white);font-weight:700;font-size:22px;line-height:30px}
  .foot-band{position:absolute;left:0;top:1033px;width:100%;height:44px;background:var(--sun-pale)}
</style>
</head>
<body>
<main class="flyer">
  <div class="header-band"></div>
  <div class="header-edge"></div>
  <div class="globe-deco globe-top" role="img" aria-label="Faint wireframe globe decoration"></div>
  <p class="headline">Schedule Your Child's Interviews<br>with the Boarding Schools</p>

  <div class="photo-frame">
    <div class="portrait" role="img" aria-label="Portrait photo of a smiling student"></div>
    <div class="portrait" role="img" aria-label="Portrait photo of a smiling student"></div>
    <div class="portrait" role="img" aria-label="Portrait photo of a smiling student"></div>
    <div class="portrait" role="img" aria-label="Portrait photo of a smiling student"></div>
    <div class="portrait" role="img" aria-label="Portrait photo of a smiling student"></div>
    <div class="portrait" role="img" aria-label="Portrait photo of a smiling student"></div>
  </div>
  <div class="brand-badge"><span class="brand-dot"></span><span class="brand-name">TPW Advisors</span></div>

  <h1 class="event-title">Brightpath Residential Academies Expo<br>East Africa 2018</h1>

  <div class="globe-deco globe-mid" role="img" aria-label="Faint wireframe globe decoration"></div>
  <div class="country-band"></div>

  <section class="stop" style="left:40px;top:506px">
    <div class="stop-name">Rwanda</div>
    <div class="flag-card">
      <svg viewBox="0 0 168 114" role="img" aria-label="Flag of Rwanda">
        <rect width="168" height="57" fill="var(--rw-blue)"/>
        <rect y="57" width="168" height="28.5" fill="var(--rw-yellow)"/>
        <rect y="85.5" width="168" height="28.5" fill="var(--rw-green)"/>
        <circle cx="136" cy="24" r="10" fill="var(--rw-yellow)"/>
      </svg>
    </div>
    <div class="stop-dates">February 6th-8th</div>
    <div class="stop-details">
      <b>Kigali School Fair:</b> February 7th, 1:30-5:30PM<br>
      <b>Student Interviews:</b> February 8th, 9:00-1PM<br>
      <b>Location:</b> Kigali Moravel Hotel
    </div>
  </section>

  <section class="stop" style="left:232px;top:506px">
    <div class="stop-name">Kenya</div>
    <div class="flag-card">
      <svg viewBox="0 0 168 114" role="img" aria-label="Flag of Kenya">
        <rect width="168" height="114" fill="var(--white)"/>
        <rect width="168" height="34" fill="var(--ke-black)"/>
        <rect y="40" width="168" height="34" fill="var(--ke-red)"/>
        <rect y="80" width="168" height="34" fill="var(--ke-green)"/>
        <ellipse cx="84" cy="57" rx="13" ry="30" fill="var(--ke-red)" stroke="var(--ke-black)" stroke-width="3"/>
      </svg>
    </div>
    <div class="stop-dates">February 9th-10th</div>
  </section>

  <section class="stop" style="left:427px;top:506px">
    <div class="stop-name">Uganda</div>
    <div class="flag-card">
      <svg viewBox="0 0 168 114" role="img" aria-label="Flag of Uganda">
        <rect width="168" height="19" fill="var(--ug-black)"/>
        <rect y="19" width="168" height="19" fill="var(--ug-yellow)"/>
        <rect y="38" width="168" height="19" fill="var(--ug-red)"/>
        <rect y="57" width="168" height="19" fill="var(--ug-black)"/>
        <rect y="76" width="168" height="19" fill="var(--ug-yellow)"/>
        <rect y="95" width="168" height="19" fill="var(--ug-red)"/>
        <circle cx="84" cy="57" r="18" fill="var(--white)"/>
      </svg>
    </div>
    <div class="stop-dates">February 11th-12th</div>
  </section>

  <div class="features">
    <b>Features:</b> *6 US Boarding Schools representative<br>
    *Learn about the application process and apply in person.<br>
    * Bring your transcripts/school reports to Interview
  </div>
  <div class="services">
    •&nbsp;&nbsp; Educational Services to Students and Families &nbsp;&nbsp;•&nbsp;&nbsp; School Tours and Fairs &nbsp;&nbsp;•<br>
    •&nbsp;&nbsp; Institutional Support &nbsp;&nbsp;•
  </div>

  <div class="contact-band"></div>
  <div class="globe-deco globe-foot" role="img" aria-label="Faint wireframe globe decoration"></div>
  <address class="contact" style="font-style:normal">
    Phone: +250795142867<br>
    Email: info@tpwadvisors.com<br>
    www.tpwlearningadvisors.com
  </address>
  <div class="foot-band"></div>
</main>
</body>
</html>
```